Clay Sparrow- Hand made fashion accessories

Clay sparrow is a new business that will be selling hand made fashion accessories for women such as bags, baskets, knecklaces etc. The items are all hand made from Africa. I would like natural colors leaning more to the cardboard rustic look. I would like the card to look simple but elegant at the same time.

Industry/Entity Type

Business

Contact Information for Business Card

www.claysparrow-example.com.au
sales@claysparrow-example.com.au
Tel: 0452867310

Font styles to use
Decorative
Script

Requirements
Must have
• Earthy and rustic colours. Straw, cardboard etc. Fine black cursive print. One side of card only name
• second side website, email and tel.
Should not have
• No need to have any description of what business sells or does. No pictures of anything.

```html
<!DOCTYPE html>
<html lang="en">
<head>
<meta charset="utf-8">
<title>Clay Sparrow – Business Card</title>
<link rel="stylesheet" href="https://fonts.googleapis.com/css2?family=Cormorant+Garamond:ital,wght@0,500;1,500&display=swap">
<style>
  :root {
    --backdrop: #2b2b2b;
    --card-light: #e0ded9;
    --card-mid: #d3d0ca;
    --card-swoosh: #a8a8a6;
    --logo-top: #eeedea;
    --logo-bottom: #c8c5bb;
    --ring: #b9b6b0;
    --ink: #111111;
    --icon: #ffffff;
  }
  html, body {
    margin: 0;
    width: 1200px;
    height: 675px;
    overflow: hidden;
    background: var(--backdrop);
  }
  .stage {
    position: relative;
    width: 1200px;
    height: 675px;
  }
  .card {
    position: absolute;
    box-shadow: 0 3px 6px rgba(0,0,0,0.6);
  }
  .card svg { display: block; }
  .card--contact { left: 340px; top: 48px; width: 554px; height: 265px; }
  .card--name { left: 338px; top: 362px; width: 556px; height: 268px; }
  .contact-text {
    font-family: "Cormorant Garamond", serif;
    font-style: italic;
    font-weight: 500;
    fill: var(--ink);
  }
  .brand-name {
    font-family: "Cormorant Garamond", serif;
    font-style: normal;
    font-weight: 500;
    font-size: 34px;
    fill: var(--ink);
  }
</style>
</head>
<body>
<main class="stage">
  <section class="card card--contact" aria-label="Contact side">
    <svg width="554" height="265" viewBox="0 0 554 265">
      <defs>
        <linearGradient id="contactFill" x1="0" y1="0" x2="0" y2="1">
          <stop offset="0" stop-color="var(--card-light)"/>
          <stop offset="1" stop-color="var(--card-mid)"/>
        </linearGradient>
      </defs>
      <rect width="554" height="265" fill="url(#contactFill)"/>
      <path class="swoosh swoosh--top" d="M0,0 L142,0 Q30,45 0,175 Z" fill="var(--card-swoosh)"/>
      <path class="swoosh swoosh--bottom" d="M554,125 Q480,225 305,265 L554,265 Z" fill="var(--card-swoosh)"/>

      <g class="icon icon--phone" fill="none" stroke="var(--icon)" stroke-width="1.6">
        <rect x="270" y="69" width="12" height="21" rx="2"/>
        <line x1="270" y1="86" x2="282" y2="86"/>
      </g>
      <text class="contact-text" x="277" y="110" font-size="14" text-anchor="middle">0452867310</text>

      <g class="icon icon--mail" fill="var(--icon)">
        <rect x="268" y="132" width="18" height="11"/>
        <path d="M268,132 L277,139 L286,132" fill="none" stroke="var(--card-mid)" stroke-width="1"/>
      </g>
      <text class="contact-text" x="277" y="165" font-size="14" text-anchor="middle">sales@claysparrow-example.com.au</text>

      <g class="icon icon--globe" fill="none" stroke="var(--icon)" stroke-width="1.3">
        <circle cx="27" cy="240" r="8"/>
        <ellipse cx="27" cy="240" rx="3.5" ry="8"/>
        <line x1="19" y1="240" x2="35" y2="240"/>
        <line x1="21" y1="235.5" x2="33" y2="235.5"/>
        <line x1="21" y1="244.5" x2="33" y2="244.5"/>
      </g>
      <text class="contact-text" x="44" y="245" font-size="16">www.claysparrow-example.com.au</text>
    </svg>
  </section>

  <section class="card card--name" aria-label="Name side">
    <svg width="556" height="268" viewBox="0 0 556 268">
      <defs>
        <linearGradient id="nameFill" x1="0" y1="0" x2="0" y2="1">
          <stop offset="0" stop-color="var(--logo-top)"/>
          <stop offset="1" stop-color="var(--logo-bottom)"/>
        </linearGradient>
      </defs>
      <rect width="556" height="268" fill="url(#nameFill)"/>
      <ellipse class="name-ring" cx="278" cy="129" rx="106" ry="82" fill="none" stroke="var(--ring)" stroke-width="1.5"/>
      <text class="brand-name" x="278" y="141" text-anchor="middle">Clay Sparrow</text>
    </svg>
  </section>
</main>
</body>
</html>
```